Web Design Project

We are an IT System Integrator. We provide Norvik 500 ERP System, CRM etc. We also provide hardware, networking servicing. Please look at www.brinquot.com.sg. They provide the same service as us. We like to redesign our web site. I will attached the color that I prefer for reference.

Our website is www.ravdu.com.sg.  It has been created about 14 years ago.  We are trying to revamp it with a new look and information.   The new website must be informative, fast.    I have attached an attachment which show the color that I prefer(brownish golden).   

Our competitor (www.brinquot.com) is carrying the same trade as us.  They have all the informations In their website that we will like to have.  Therefore I recommend you to take a look at my competitor website and have a better   
understanding on the kind of information I would like to have for my new website.

This project is guarantee to the person with the best design.  We can have it guarantee.

Target Market(s)

Corporate and companies

Industry/Entity Type

Hardware

```html
<!DOCTYPE html>
<html lang="en">
<head>
<meta charset="utf-8">
<title>Ravdu Information Systems Pte Ltd</title>
<link rel="stylesheet" href="https://fonts.googleapis.com/css2?family=Arimo:ital,wght@0,400;0,700;1,400&family=PT+Sans:wght@400;700&display=swap">
<style>
:root{
  --orange:#c87a34;
  --orange-text:#c86f24;
  --band-top:#c9793a;
  --band-bottom:#b9803f;
  --gold:#f7b733;
  --ink:#2f2f2f;
  --grey:#666;
  --paper:#f4f4f4;
  --footer:#7b7b7b;
  --white:#fff;
}
*{box-sizing:border-box;margin:0;padding:0}
html,body{width:1200px;height:1001px;overflow:hidden}
body{position:relative;background:var(--paper);font-family:"Arimo",Arial,sans-serif;color:var(--ink)}
.header{position:absolute;left:0;top:0;width:1200px;height:90px;background:var(--white);border-bottom:2px solid #ddd}
.brand-mark{position:absolute;left:222px;top:22px;display:flex;align-items:center;gap:8px;font-weight:700;font-size:38px;line-height:44px;color:var(--orange)}
.brand-mark .dot{width:14px;height:14px;border-radius:50%;background:var(--orange)}
.brand-name{position:absolute;left:380px;top:38px;white-space:nowrap;font-size:20px;font-weight:700;font-style:italic;color:#555}
.callus{position:absolute;right:230px;top:20px;font-size:10px;color:#888;white-space:nowrap}
.callus b{font-weight:400;color:#333;font-size:11px;margin-left:3px}
.util-rule{position:absolute;left:778px;top:47px;width:200px;border-top:1px solid #e3e3e3}
.util{position:absolute;top:61px;font-size:10px;line-height:10px;color:var(--orange-text);white-space:nowrap}
.util::before{content:"";display:inline-block;width:4px;height:4px;border-radius:50%;background:var(--orange);margin-right:5px;vertical-align:middle}
.band{position:absolute;left:0;top:92px;width:1200px;height:251px;background:linear-gradient(var(--band-top),var(--band-bottom))}
.nav-item{position:absolute;top:107px;font-family:"PT Sans",sans-serif;font-size:13.5px;line-height:16px;color:var(--white);white-space:nowrap;text-decoration:none}
.nav-item.active{color:var(--gold)}
.nav-sep{position:absolute;top:107px;font-family:"PT Sans",sans-serif;font-size:12px;line-height:16px;color:var(--white)}
.social{position:absolute;left:1042px;top:192px;display:flex;flex-direction:column;gap:17px}
.social span{width:14px;height:14px;background:var(--white);border-radius:2px}
.slider{position:absolute;left:221px;top:136px;width:758px;height:283px;background:var(--white);box-shadow:0 4px 10px rgba(0,0,0,.18)}
.slide-photo{position:absolute;left:8px;top:7px;width:742px;height:268px;background:linear-gradient(120deg,#8a9ea6 0%,#c9b8a6 35%,#7c6a5d 55%,#d0d0cc 80%,#a9aeb0 100%)}
.caption{position:absolute;left:546px;top:158px;width:204px;height:50px;background:rgba(60,60,60,.8);color:var(--white);font-size:14px;line-height:17px;padding:8px 0 0 25px;white-space:nowrap}
.dots{position:absolute;left:548px;top:440px;display:flex;gap:9px}
.dots span{width:13px;height:13px;border-radius:50%;background:#bbb;border:2px solid #e6e6e6}
.dots span.on{background:var(--orange)}
.welcome{position:absolute;left:222px;top:492px;width:505px}
.welcome h1{font-weight:400;font-size:18px;color:var(--orange-text);margin-bottom:10px;white-space:nowrap}
.welcome p{font-size:10px;line-height:14.5px;color:#333;margin-bottom:14.5px}
.card{position:absolute;background:var(--white);box-shadow:0 2px 4px rgba(0,0,0,.15)}
.card h2{font-weight:400;font-size:17px;color:#555;margin:17px 0 0 26px;white-space:nowrap}
.news{left:752px;top:494px;width:226px;height:184px}
.news-item{display:flex;gap:9px;margin:14px 0 0 27px}
.date{width:23px;height:29px;text-align:center;font-size:7px;color:var(--white);flex:none}
.date .m{background:#666;height:9px;line-height:9px}
.date .d{background:var(--orange);height:20px;font-size:8px;padding-top:3px;line-height:8px}
.news h3{font-size:10.5px;color:var(--orange-text);line-height:12.5px;font-weight:700}
.news p{margin:6px 16px 0 27px;font-size:10px;line-height:12px;color:#555}
.news-brand{margin:10px 0 0 26px;display:flex;align-items:center;gap:6px;font-size:12px;font-weight:700;color:#333}
.news-brand i{width:16px;height:16px;background:#5460a8}
.testimonials{left:222px;top:718px;width:226px;height:183px}
.quote{position:absolute;left:28px;top:60px;width:182px;font-size:10px;line-height:12.2px;font-style:italic;color:#555}
.qmark{position:absolute;font-size:40px;color:#ddd;font-family:Georgia,serif}
.by{position:absolute;left:25px;top:139px;font-size:9px;font-weight:700;color:var(--orange-text);white-space:nowrap}
.partners{left:486px;top:718px;width:226px;height:183px}
.partner-badge{position:absolute;left:26px;top:57px;width:172px;height:105px;border:1px solid #ddd;display:flex;align-items:center;justify-content:center}
.partner-badge span{width:114px;height:30px;border-radius:15px;background:#0b7a4a}
.contact{left:752px;top:718px;width:226px;height:183px}
.contact .lines{position:absolute;left:29px;top:55px;font-size:10px;line-height:14.5px;color:#555;white-space:nowrap}
.contact .lines b{color:var(--orange-text)}
.contact .tel{position:absolute;left:30px;top:123px;font-size:10px;line-height:21.5px;color:#555;white-space:nowrap}
.footer{position:absolute;left:0;top:942px;width:1200px;height:59px;background:var(--footer);border-top:4px solid var(--orange)}
.copy{position:absolute;left:222px;top:27px;font-size:9px;color:var(--white);white-space:nowrap}
.links{position:absolute;right:222px;top:27px;font-size:9px;color:#e4e4e4;white-space:nowrap}
.links span{margin:0 6px}
</style>
</head>
<body>
<header class="header">
  <div class="brand-mark"><span>RIS</span><span class="dot"></span></div>
  <div class="brand-name">Ravdu Information Systems Pte Ltd</div>
  <div class="callus"><em>Call Us Today:</em><b>(065) 6120-4470</b></div>
  <div class="util-rule"></div>
  <span class="util" style="left:778px">Log In</span>
  <span class="util" style="left:824px">Enquiry</span>
  <span class="util" style="left:876px">Support</span>
  <span class="util" style="left:930px">Contact</span>
</header>

<div class="band"></div>
<nav>
  <a class="nav-item active" style="left:228px">HOME</a><span class="nav-sep" style="left:286px">/</span>
  <a class="nav-item" style="left:310px">COMPANY</a><span class="nav-sep" style="left:392px">/</span>
  <a class="nav-item" style="left:416px">PRODUCTS</a><span class="nav-sep" style="left:504px">/</span>
  <a class="nav-item" style="left:526px">LEDGRA</a><span class="nav-sep" style="left:594px">/</span>
  <a class="nav-item" style="left:618px">SERVICES</a><span class="nav-sep" style="left:696px">/</span>
  <a class="nav-item" style="left:720px">CLIENTELE</a><span class="nav-sep" style="left:806px">/</span>
  <a class="nav-item" style="left:828px">CAREERS</a><span class="nav-sep" style="left:903px">/</span>
  <a class="nav-item" style="left:928px">INFOBIN</a>
</nav>
<div class="social" aria-label="Social links"><span></span><span></span><span></span><span></span></div>

<section class="slider">
  <div class="slide-photo" role="img" aria-label="Photo of a team of colleagues working together at computer screens in an office"></div>
  <div class="caption">End-to-End Business<br>Management Applications</div>
</section>
<div class="dots"><span class="on"></span><span></span><span></span><span></span><span></span></div>

<section class="welcome">
  <h1>Welcome to Ravdu Information Systems Pte Ltd (RIS)</h1>
  <p><b>Ravdu Information Systems Pte Ltd (RIS)</b> is professionally managed by a core group of visionaries and technologists with decades of industry experience between them and backed by a team of trained professionals at all levels of operations. Perfection is a way of life at RIS. The organization has grown from a small beginning in 1993, to become a company of international repute for reliability. RIS has transformed from an LEDGRA Reseller to a company providing total IT solutions to companies in Singapore and the Asia region. RIS provides hardware maintenance, networking, software and consulting services.</p>
  <p>We have a large customer base, which spreads across Singapore, South East Asia and East Asia. This illustrates RIS is able to offer overseas support to customers who have regional operations. We also have several listed companies as customers, as shown in our track record. " We are the authorized LEDGRA Business Partner and Certified Consultant by Ledgra International</p>
</section>

<aside class="card news">
  <h2>Recent News</h2>
  <div class="news-item">
    <div class="date"><div class="m">Aug</div><div class="d">04<br>2013</div></div>
    <h3>Expanding the Boundaries<br>with Quillix-ERP<br>Integration workshop.</h3>
  </div>
  <p>You are invited to attend the Expanding the Boundaries with Quillix-ERP Integration workshop. There are many functions and values offers</p>
  <div class="news-brand"><i></i>Quillix</div>
</aside>

<section class="card testimonials">
  <h2>Our Testimonials</h2>
  <span class="qmark" style="left:0;top:40px">&ldquo;</span>
  <p class="quote">We wish to place on record our thanks and appreciation for the prompt services and personal attention provided by Mr Tan Wei Loong from Ravdu Information Systems Pte Ltd...</p>
  <span class="by">~ Accountant at Lumen Crafts Pte Ltd</span>
  <span class="qmark" style="left:205px;top:125px">&rdquo;</span>
</section>

<section class="card partners">
  <h2>Our Partners</h2>
  <div class="partner-badge" role="img" aria-label="Partner badge"><span></span></div>
</section>

<section class="card contact">
  <h2>Contact Us Today!</h2>
  <div class="lines"><b>Ravdu Information Systems Pte Ltd</b><br>18 Orchid Vale Road<br>#03-12/14 Fernhill Centre<br>Singapore - 579211</div>
  <div class="tel">Telphone: (065) 6120-4470<br>Facsimile No: (065) 6120-4477</div>
</section>

<footer class="footer">
  <div class="copy">Copyright &copy; 2013 <b>Ravdu Information Systems Pte Ltd</b>. All rights reserved.</div>
  <div class="links">Terms &amp; Conditions<span>|</span>Privacy Policy<span>|</span>Sitemap</div>
</footer>
</body>
</html>
```